Updated DJ business Card showing other businesses

DJ Kestro offers professional mobile dj services including DJ. MC. Karaoke.
Silent Disco (will attach logo)
I also offer a 360 Photo Booth.

Contact info:
(555) 314-7720
lenny.corbitt@mailvane.net
Social Media @DJKestroBPZ

```html
<!DOCTYPE html>
<html lang="en">
<head>
<meta charset="utf-8">
<title>DJ Kestro Business Card</title>
<link rel="stylesheet" href="https://fonts.googleapis.com/css2?family=Jost:wght@400;500;600;700&display=swap">
<style>
  :root {
    --stage: #d3d3d3;
    --brand-red: #d41f45;
    --ink: #111111;
    --paper: #ffffff;
    --muted: #2a2a2a;
  }
  * { box-sizing: border-box; margin: 0; padding: 0; }
  html, body {
    width: 1200px; height: 913px; overflow: hidden;
    background: var(--stage);
    font-family: "Jost", "Futura", sans-serif;
  }
  .stage {
    width: 1200px; height: 913px;
    display: flex; flex-direction: column; align-items: center; justify-content: center;
    gap: 56px;
  }
  .card {
    width: 640px; height: 366px;
    position: relative;
    box-shadow: 0 10px 28px rgba(0,0,0,0.18);
  }

  /* Front */
  .card-front {
    background: var(--paper);
    border: 2px solid var(--brand-red);
    padding: 34px 40px 28px 44px;
  }
  .brand-name {
    font-weight: 700; font-size: 62px; line-height: 1;
    color: var(--brand-red); letter-spacing: -0.5px;
  }
  .services-intro {
    margin-top: 10px;
    font-weight: 600; font-size: 21px; color: var(--ink);
  }
  .services-list {
    margin-top: 6px;
    font-weight: 600; font-size: 33px; color: var(--brand-red);
    letter-spacing: 0.5px;
  }
  .booth-band {
    margin-top: 14px;
    width: 520px; height: 48px; border-radius: 24px;
    background: var(--brand-red); color: var(--paper);
    display: flex; align-items: center; padding-left: 30px;
    font-weight: 600; font-size: 26px;
  }
  .card-footer {
    position: absolute; left: 44px; right: 40px; bottom: 28px;
    display: flex; justify-content: space-between; align-items: flex-end;
  }
  .sub-brand {
    display: flex; align-items: center; gap: 10px;
    font-weight: 700; font-size: 24px; color: var(--ink);
  }
  .sub-brand-dot { width: 34px; height: 34px; border-radius: 50%; background: var(--ink); }
  .contact-list { list-style: none; font-size: 17px; font-weight: 400; color: var(--muted); line-height: 1.45; }
  .contact-list li { display: flex; align-items: center; gap: 7px; }
  .contact-icon { width: 14px; height: 14px; fill: var(--brand-red); flex: none; }

  /* Back */
  .card-back {
    background: var(--brand-red);
    display: flex; align-items: center; justify-content: center;
  }
  .back-mark {
    display: flex; align-items: center; gap: 22px;
    font-weight: 700; font-size: 76px; color: var(--paper);
    text-transform: uppercase; letter-spacing: 1px;
  }
  .back-mark-dot { width: 96px; height: 96px; border-radius: 50%; background: var(--ink); }
</style>
</head>
<body>
<main class="stage">
  <section class="card card-front" aria-label="Business card front">
    <h1 class="brand-name">DJ Kestro</h1>
    <p class="services-intro">offers professional Mobile Dj Services including</p>
    <p class="services-list">DJ. MC. Karaoke</p>
    <p class="booth-band">I also offer a 360 Photo Booth.</p>
    <div class="card-footer">
      <div class="sub-brand"><span class="sub-brand-dot"></span>Silent Disco</div>
      <ul class="contact-list">
        <li>
          <svg class="contact-icon" viewBox="0 0 24 24" aria-hidden="true"><path d="M6.6 10.8a15.2 15.2 0 0 0 6.6 6.6l2.2-2.2a1 1 0 0 1 1-.25 11.4 11.4 0 0 0 3.6.57 1 1 0 0 1 1 1V20a1 1 0 0 1-1 1A17 17 0 0 1 3 4a1 1 0 0 1 1-1h3.5a1 1 0 0 1 1 1c0 1.25.2 2.45.57 3.57a1 1 0 0 1-.25 1z"/></svg>
          (555) 314-7720
        </li>
        <li>
          <svg class="contact-icon" viewBox="0 0 24 24" aria-hidden="true"><path d="M2 5h20v14H2z M2 5l10 8 10-8" /></svg>
          lenny.corbitt@mailvane.net
        </li>
        <li>Social Media @DJKestroBPZ</li>
      </ul>
    </div>
  </section>

  <section class="card card-back" aria-label="Business card back">
    <div class="back-mark"><span class="back-mark-dot"></span>Silent Disco</div>
  </section>
</main>
</body>
</html>
```